Lumo Sound Bazaar Design - platform for listeners to invest in the artists they love

We need a preview of a couple pages of what our app might look like to put on our website before launch. It is a Music streaming platform and NFT marketplace where users can invest in artists and own music royalties. there needs to be a user profile and portfolio showing returns for their collections. the NFT exchange should have artists and NFT listings with album art, the home page can be similar to tunevale we need pages for mobile and desktop version.

For inspiration look at;
tunevale
plaxmint
quorbly

should be similar to a tunevale and quorbly mashup

some images are attached for ideas

Target Market(s)

Crypto native musicians/listeners

Industry/Entity Type

Music streaming/ NFT

Font styles to use
Other font styles liked:
• Arial

Requirements
Must have
• Must have a place to buy/sell NFTs listen to music/ check portfolio performance and collection
Nice to have
• a percent gain and loss on the NFTs someone owns would be nice smooth easy to use design

```html
<!DOCTYPE html>
<html lang="en">
<head>
<meta charset="utf-8">
<title>Lumo Sound Bazaar – App Screens</title>
<link rel="stylesheet" href="https://fonts.googleapis.com/css2?family=Inter:wght@400;500;600;700&display=swap">
<style>
:root{
  --canvas:#ffffff;
  --screen:#141414;
  --panel:#1f1f1f;
  --nav:#181818;
  --line:#2a2a2a;
  --text:#ffffff;
  --muted:#a6a6a6;
  --dim:#7a7a7a;
  --blue:#3d7bf2;
  --green:#4ccb4c;
  --teal:#0e5a78;
  --mint:#27d89e;
  --gold:#e0b400;
  --violet:#7b45e8;
  --sky:#82dcea;
  --cream:#e4e4a8;
  --plum:#3a2870;
}
*{margin:0;padding:0;box-sizing:border-box}
html,body{width:1200px;height:781px;overflow:hidden;background:var(--canvas)}
body{position:relative;font-family:"Inter",Arial,sans-serif;color:var(--text)}
.screen{position:absolute;top:60px;width:311px;height:675px;background:var(--screen);border-radius:24px;overflow:hidden}
.screen--home{left:69px}
.screen--market{left:442px}
.screen--portfolio{left:815px}
.abs{position:absolute}
.header-title{position:absolute;left:0;right:0;top:12px;text-align:center;font-size:18px;font-weight:700}
.divider{position:absolute;left:0;right:0;top:45px;height:1px;background:var(--line)}
.search{position:absolute;height:29px;background:var(--panel);border-radius:6px;display:flex;align-items:center;padding-left:8px;gap:7px;font-size:10.5px;color:var(--dim)}
.section-title{position:absolute;left:15px;font-size:15px;font-weight:600;line-height:18px}
.tile{position:absolute;width:102px;height:102px;border-radius:4px}
.tile-title{position:absolute;font-size:11px;font-weight:600;line-height:13px;white-space:nowrap}
.tile-sub{position:absolute;font-size:9px;color:var(--muted);line-height:11px;white-space:nowrap}
.artist-photo{position:absolute;top:273px;width:96px;height:96px;border-radius:3px}
.avatar{position:absolute;border-radius:50%}
.artist-name{position:absolute;top:392px;width:96px;text-align:center;font-size:10px;font-weight:600}
.row-thumb{position:absolute;left:15px;width:43px;height:43px;border-radius:3px}
.row-title{position:absolute;left:69px;font-size:11px;font-weight:600;line-height:13px}
.row-sub{position:absolute;left:69px;font-size:9px;color:var(--muted);line-height:11px}
.row-menu{position:absolute;left:293px;width:3px;display:flex;flex-direction:column;gap:2.5px}
.row-menu i{width:2.5px;height:2.5px;border-radius:50%;background:#d0d0d0}
.gain{color:var(--green)}
.nav{position:absolute;left:0;right:0;bottom:0;height:45px;background:var(--nav);border-top:1px solid var(--line)}
.nav-item{position:absolute;top:6px;width:60px;margin-left:-30px;text-align:center;font-size:9.5px;color:var(--dim)}
.nav-item svg{display:block;margin:0 auto 1px;width:16px;height:16px}
.nav-item--active{color:var(--blue)}
.periods{position:absolute;left:15px;top:401px;width:281px;height:31px;background:var(--panel);border-radius:4px;display:flex}
.period{flex:1;display:flex;align-items:center;justify-content:center;font-size:10.5px;font-weight:500}
.period--active{background:var(--blue);border-radius:3px}
.axis{position:absolute;font-size:7.5px;color:var(--dim);width:20px;margin-left:-10px;text-align:center}
</style>
</head>
<body>

<!-- HOME -->
<section class="screen screen--home">
  <div class="search" style="left:15px;top:9px;width:254px">
    <svg width="11" height="11" viewBox="0 0 12 12" fill="none" stroke="#8a8a8a" stroke-width="1.4"><circle cx="5" cy="5" r="4"/><path d="M8 8l3 3"/></svg>Search Anything...
  </div>
  <svg class="abs" style="left:282px;top:14px" width="14" height="15" viewBox="0 0 14 15"><path d="M7 1.5c-2.5 0-4 1.8-4 4.2v3L1.5 11h11L11 8.7v-3C11 3.3 9.5 1.5 7 1.5z" fill="#fff"/><rect x="5.3" y="12" width="3.4" height="2" rx="1" fill="#fff"/><circle cx="10.5" cy="2.5" r="2.2" fill="#ff2d2d"/></svg>
  <div class="divider"></div>

  <h2 class="section-title" style="top:61px">My Collections</h2>
  <div class="tile" role="img" aria-label="Album art: illustrated character on teal" style="left:15px;top:87px;background:var(--teal)"></div>
  <div class="tile" role="img" aria-label="Album art: illustrated character on mint" style="left:126px;top:87px;background:var(--mint)"></div>
  <div class="tile" role="img" aria-label="Album art: illustrated character on gold" style="left:237px;top:87px;background:var(--gold)"></div>
  <div class="tile-title" style="left:15px;top:195px">Open Skyline</div><div class="tile-sub" style="left:15px;top:209px">Ray Veldon</div>
  <div class="tile-title" style="left:126px;top:195px">Open Skyline</div><div class="tile-sub" style="left:126px;top:209px">Ray Veldon</div>
  <div class="tile-title" style="left:237px;top:195px">Open Skyline</div><div class="tile-sub" style="left:237px;top:209px">Ray Veldon</div>

  <h2 class="section-title" style="top:247px">Followed Artist</h2>
  <div class="artist-photo" role="img" aria-label="Concert photo: saxophonist under red and blue light" style="left:15px;background:linear-gradient(120deg,#b3141e 0%,#5a1030 50%,#0c5a8a 100%)"></div>
  <div class="artist-photo" role="img" aria-label="Concert photo: musicians on a teal lit stage" style="left:120px;background:linear-gradient(160deg,#0d7f86 0%,#1c3a5a 55%,#2a2450 100%)"></div>
  <div class="artist-photo" role="img" aria-label="Concert photo: crowd and stage lights" style="left:225px;background:linear-gradient(180deg,#3a3530 0%,#8a5a30 50%,#5a1a14 100%)"></div>
  <div class="avatar" role="img" aria-label="Artist avatar" style="left:46px;top:351px;width:35px;height:35px;background:var(--teal)"></div>
  <div class="avatar" role="img" aria-label="Artist avatar" style="left:151px;top:351px;width:35px;height:35px;background:var(--plum)"></div>
  <div class="avatar" role="img" aria-label="Artist avatar" style="left:256px;top:351px;width:35px;height:35px;background:var(--violet)"></div>
  <div class="artist-name" style="left:15px">Volt Parade</div>
  <div class="artist-name" style="left:120px">Ray Veldon</div>
  <div class="artist-name" style="left:225px">Hollow Bloom</div>

  <h2 class="section-title" style="top:430px">Recently Played</h2>
  <div class="row-thumb" role="img" aria-label="Track art on gold" style="top:457px;background:var(--gold)"></div>
  <div class="row-title" style="top:467px">Kind Hound</div><div class="row-sub" style="top:481px">Mira Kessel</div>
  <div class="row-menu" style="top:470px"><i></i><i></i><i></i></div>
  <div class="row-thumb" role="img" aria-label="Track art on cream" style="top:510px;background:var(--cream)"></div>
  <div class="row-title" style="top:520px">Kind Hound</div><div class="row-sub" style="top:534px">Mira Kessel</div>
  <div class="row-menu" style="top:523px"><i></i><i></i><i></i></div>
  <div class="row-thumb" role="img" aria-label="Track art on violet" style="top:562px;background:var(--violet)"></div>
  <div class="row-title" style="top:572px">Kind Hound</div><div class="row-sub" style="top:586px">Mira Kessel</div>
  <div class="row-menu" style="top:575px"><i></i><i></i><i></i></div>

  <nav class="nav">
    <div class="nav-item nav-item--active" style="left:47px"><svg viewBox="0 0 16 16"><path d="M8 1L1 7v8h5v-5h4v5h5V7z" fill="currentColor"/></svg>Home</div>
    <div class="nav-item" style="left:119px"><svg viewBox="0 0 16 16"><path d="M5 5V4a3 3 0 016 0v1h3l-1 10H3L2 5z" fill="currentColor"/></svg>Market</div>
    <div class="nav-item" style="left:192px"><svg viewBox="0 0 16 16" fill="currentColor"><rect x="1" y="6" width="3" height="9" rx="1"/><rect x="6.5" y="9" width="3" height="6" rx="1"/><rect x="12" y="1" width="3" height="14" rx="1"/></svg>Stat</div>
    <div class="nav-item" style="left:264px"><svg viewBox="0 0 16 16" fill="currentColor"><circle cx="8" cy="4.5" r="3.5"/><path d="M1 15c0-3.5 3-6 7-6s7 2.5 7 6z"/></svg>Profile</div>
  </nav>
</section>

<!-- MARKETPLACE -->
<section class="screen screen--market">
  <h1 class="header-title">Marketplace</h1>
  <div class="divider"></div>
  <div class="search" style="left:15px;top:60px;width:281px">
    <svg width="11" height="11" viewBox="0 0 12 12" fill="none" stroke="#8a8a8a" stroke-width="1.4"><circle cx="5" cy="5" r="4"/><path d="M8 8l3 3"/></svg>Search Anything...
  </div>

  <h2 class="section-title" style="top:103px">Trending Collections</h2>
  <div class="tile" role="img" aria-label="Album art: illustrated character on teal" style="left:15px;top:130px;background:var(--teal)"></div>
  <div class="tile" role="img" aria-label="Album art: illustrated character on mint" style="left:126px;top:130px;background:var(--mint)"></div>
  <div class="tile" role="img" aria-label="Album art: illustrated character on gold" style="left:237px;top:130px;background:var(--gold)"></div>
  <div class="tile-title" style="left:15px;top:238px">Open Skyline</div><div class="tile-sub" style="left:15px;top:252px">Ray Veldon</div>
  <div class="tile-title" style="left:126px;top:238px">Open Skyline</div><div class="tile-sub" style="left:126px;top:252px">Ray Veldon</div>
  <div class="tile-title" style="left:237px;top:238px">Open Skyline</div><div class="tile-sub" style="left:237px;top:252px">Ray Veldon</div>

  <h2 class="section-title" style="top:290px">Popular Artist</h2>
  <div class="avatar" role="img" aria-label="Artist avatar" style="left:15px;top:316px;width:38px;height:38px;background:var(--teal)"></div>
  <div class="tile-title" style="left:62px;top:324px">Ray Veldon</div><div class="tile-sub gain" style="left:62px;top:338px">+2,45%</div>
  <div class="avatar" role="img" aria-label="Artist avatar" style="left:150px;top:316px;width:38px;height:38px;background:var(--mint)"></div>
  <div class="tile-title" style="left:197px;top:324px">Ray Veldon</div><div class="tile-sub gain" style="left:197px;top:338px">+2,45%</div>
  <div class="avatar" role="img" aria-label="Artist avatar" style="left:286px;top:316px;width:38px;height:38px;background:var(--violet)"></div>
  <div class="avatar" role="img" aria-label="Artist avatar" style="left:15px;top:366px;width:38px;height:38px;background:var(--gold)"></div>
  <div class="tile-title" style="left:62px;top:374px">Ray Veldon</div><div class="tile-sub gain" style="left:62px;top:388px">+2,45%</div>
  <div class="avatar" role="img" aria-label="Artist avatar" style="left:150px;top:366px;width:38px;height:38px;background:var(--sky)"></div>
  <div class="tile-title" style="left:197px;top:374px">Ray Veldon</div><div class="tile-sub gain" style="left:197px;top:388px">+2,45%</div>
  <div class="avatar" role="img" aria-label="Artist avatar" style="left:286px;top:366px;width:38px;height:38px;background:var(--cream)"></div>

  <h2 class="section-title" style="top:430px">Hot Collections</h2>
  <div class="tile" role="img" aria-label="NFT art on deep plum" style="left:15px;top:456px;width:73px;height:73px;background:var(--plum)"></div>
  <div class="tile" role="img" aria-label="NFT art on violet" style="left:97px;top:456px;width:73px;height:73px;background:var(--violet)"></div>
  <div class="tile" role="img" aria-label="NFT art on sky blue" style="left:178px;top:456px;width:73px;height:73px;background:var(--sky)"></div>
  <div class="tile" role="img" aria-label="NFT art on cream" style="left:260px;top:456px;width:73px;height:73px;background:var(--cream)"></div>
  <div class="tile-title" style="left:15px;top:535px;font-size:10px">Ray Veldon</div><div class="tile-sub" style="left:15px;top:549px;font-size:8.5px">Open Skyline</div>
  <div class="tile-title" style="left:97px;top:535px;font-size:10px">Volt Parade</div><div class="tile-sub" style="left:97px;top:549px;font-size:8.5px">$145,25</div>
  <div class="tile-title" style="left:178px;top:535px;font-size:10px">Lazy Lemur</div><div class="tile-sub" style="left:178px;top:549px;font-size:8.5px">$145,25</div>
  <div class="tile-title" style="left:260px;top:535px;font-size:10px">Lazy Lemur</div><div class="tile-sub" style="left:260px;top:549px;font-size:8.5px">$145,25</div>

  <nav class="nav">
    <div class="nav-item" style="left:47px"><svg viewBox="0 0 16 16"><path d="M8 1L1 7v8h5v-5h4v5h5V7z" fill="currentColor"/></svg>Home</div>
    <div class="nav-item nav-item--active" style="left:119px"><svg viewBox="0 0 16 16"><path d="M5 5V4a3 3 0 016 0v1h3l-1 10H3L2 5z" fill="currentColor"/></svg>Market</div>
    <div class="nav-item" style="left:192px"><svg viewBox="0 0 16 16" fill="currentColor"><rect x="1" y="6" width="3" height="9" rx="1"/><rect x="6.5" y="9" width="3" height="6" rx="1"/><rect x="12" y="1" width="3" height="14" rx="1"/></svg>Stat</div>
    <div class="nav-item" style="left:264px"><svg viewBox="0 0 16 16" fill="currentColor"><circle cx="8" cy="4.5" r="3.5"/><path d="M1 15c0-3.5 3-6 7-6s7 2.5 7 6z"/></svg>Profile</div>
  </nav>
</section>

<!-- PORTFOLIO -->
<section class="screen screen--portfolio">
  <h1 class="header-title">My Portfolio</h1>
  <div class="divider"></div>
  <div class="abs" style="left:15px;top:61px;font-size:11.5px;color:#d8d8d8">John's portfolio</div>
  <div class="abs" style="right:15px;top:63px;font-size:8.5px;color:#d8d8d8">10-16 Mart ▾</div>
  <div class="abs" style="left:15px;top:76px;font-size:26px;font-weight:700">$189,00</div>
  <div class="abs gain" style="left:15px;top:107px;font-size:11.5px">+2,45%</div>

  <svg class="abs" style="left:0;top:145px" width="311" height="230" viewBox="0 145 311 230">
    <defs>
      <linearGradient id="areaFill" x1="0" y1="0" x2="0" y2="1">
        <stop offset="0" stop-color="#3d7bf2" stop-opacity="0.95"/>
        <stop offset="1" stop-color="#3d7bf2" stop-opacity="0"/>
      </linearGradient>
    </defs>
    <g stroke="#6a6a6a" stroke-width="0.7" stroke-dasharray="2 2">
      <line x1="13" y1="151" x2="13" y2="372"/><line x1="41" y1="151" x2="41" y2="372"/><line x1="70" y1="151" x2="70" y2="372"/><line x1="98" y1="151" x2="98" y2="372"/><line x1="127" y1="151" x2="127" y2="372"/><line x1="155" y1="151" x2="155" y2="372"/><line x1="184" y1="151" x2="184" y2="372"/><line x1="212" y1="151" x2="212" y2="372"/><line x1="241" y1="151" x2="241" y2="372"/><line x1="269" y1="151" x2="269" y2="372"/><line x1="298" y1="151" x2="298" y2="372"/>
    </g>
    <path d="M0 289 C5 285 10 283 13 284 C25 285 35 292 44 289 C52 286 58 275 69 274 C80 272 92 280 100 276 C108 272 112 258 120 256 C128 254 133 258 140 255 C146 252 149 245 155 246 C163 247 175 259 183 258 C193 256 198 224 204 222 C209 220 212 229 217 227 C224 224 232 209 241 209 C252 209 260 225 270 224 C280 222 288 200 298 199 C304 198 307 198 311 194 L311 375 L0 375 Z" fill="url(#areaFill)"/>
    <path d="M0 289 C5 285 10 283 13 284 C25 285 35 292 44 289 C52 286 58 275 69 274 C80 272 92 280 100 276 C108 272 112 258 120 256 C128 254 133 258 140 255 C146 252 149 245 155 246 C163 247 175 259 183 258 C193 256 198 224 204 222 C209 220 212 229 217 227 C224 224 232 209 241 209 C252 209 260 225 270 224 C280 222 288 200 298 199 C304 198 307 198 311 194" fill="none" stroke="#4a86f5" stroke-width="1.4"/>
  </svg>
  <div class="axis" style="left:13px;top:137px">62</div><div class="axis" style="left:41px;top:137px">67</div><div class="axis" style="left:70px;top:137px">72</div><div class="axis" style="left:98px;top:137px">77</div><div class="axis" style="left:127px;top:137px">82</div><div class="axis" style="left:155px;top:137px">87</div><div class="axis" style="left:184px;top:137px">92</div><div class="axis" style="left:212px;top:137px">97</div><div class="axis" style="left:241px;top:137px">102</div><div class="axis" style="left:269px;top:137px">107</div><div class="axis" style="left:298px;top:137px">112</div>
  <div class="axis" style="left:13px;top:377px">0</div><div class="axis" style="left:41px;top:377px">1</div><div class="axis" style="left:70px;top:377px">2</div><div class="axis" style="left:98px;top:377px">3</div><div class="axis" style="left:127px;top:377px">4</div><div class="axis" style="left:155px;top:377px">5</div><div class="axis" style="left:184px;top:377px">6</div><div class="axis" style="left:212px;top:377px">7</div><div class="axis" style="left:241px;top:377px">8</div><div class="axis" style="left:269px;top:377px">9</div><div class="axis" style="left:298px;top:377px">10</div>

  <div class="periods">
    <div class="period">1 Day</div>
    <div class="period period--active">5 Day</div>
    <div class="period">7 Day</div>
    <div class="period">15 Day</div>
    <div class="period">30 Day</div>
  </div>

  <h2 class="section-title" style="top:459px">My Collections</h2>
  <div class="row-thumb" role="img" aria-label="NFT art on violet" style="top:486px;background:var(--violet)"></div>
  <div class="row-title" style="left:69px;top:496px">Kind Hound</div><div class="row-sub" style="top:510px">Mira Kessel</div>
  <div class="abs gain" style="right:15px;top:502px;font-size:9px">+2,45%</div>
  <div class="row-thumb" role="img" aria-label="NFT art on cream" style="top:539px;background:var(--cream)"></div>
  <div class="row-title" style="top:549px">Kind Hound</div><div class="row-sub" style="top:563px">Mira Kessel</div>
  <div class="abs gain" style="right:15px;top:555px;font-size:9px">+2,45%</div>
  <div class="row-thumb" role="img" aria-label="NFT art on deep plum" style="top:591px;background:var(--plum)"></div>
  <div class="row-title" style="top:601px">Kind Hound</div><div class="row-sub" style="top:615px">Mira Kessel</div>
  <div class="abs gain" style="right:15px;top:607px;font-size:9px">+2,45%</div>

  <nav class="nav">
    <div class="nav-item" style="left:47px"><svg viewBox="0 0 16 16"><path d="M8 1L1 7v8h5v-5h4v5h5V7z" fill="currentColor"/></svg>Home</div>
    <div class="nav-item" style="left:119px"><svg viewBox="0 0 16 16"><path d="M5 5V4a3 3 0 016 0v1h3l-1 10H3L2 5z" fill="currentColor"/></svg>Market</div>
    <div class="nav-item nav-item--active" style="left:192px"><svg viewBox="0 0 16 16" fill="currentColor"><rect x="1" y="6" width="3" height="9" rx="1"/><rect x="6.5" y="9" width="3" height="6" rx="1"/><rect x="12" y="1" width="3" height="14" rx="1"/></svg>Stat</div>
    <div class="nav-item" style="left:264px"><svg viewBox="0 0 16 16" fill="currentColor"><circle cx="8" cy="4.5" r="3.5"/><path d="M1 15c0-3.5 3-6 7-6s7 2.5 7 6z"/></svg>Profile</div>
  </nav>
</section>

</body>
</html>
```